Brevard Consulting Stationary and Business Card
Professional Modern Stationary and Business Card Design
Brevard Consulting Stationary and Business Card -
Creative Brief
Bright & Fun-filled
Owen P. Marsh
Consultant
517 Alder Lane Larkmoor, VT 05999
owen@pelmarconsult.example
www.pelmarconsult.example
I am looking for professional business cards to be provided to educators so that they remember me and my business. I am hoping the stationary will carry the look and feel of the business card. The stationary can be simple in design but professional. Text needs to be easily modifiable in design.
I am looking to be able to add bullet points to the back of the business card. I am expecting to have 3 to 5 bullets such as: * Technology Plan Creation * Education Technology Support * Teacher Professional Development * Budgeting * IT Support to help with business processes

```html
<!DOCTYPE html>
<html lang="en">
<head>
<meta charset="utf-8">
<title>Brevard Consulting Stationery and Business Card</title>
<link href="https://fonts.googleapis.com/css2?family=Montserrat:wght@400;600;700&display=swap" rel="stylesheet">
<style>
:root{
  --blue:#1d3f96;
  --brand:#1b7fc0;
  --green:#7cc242;
  --ink:#3a3a3a;
  --paper:#ffffff;
  --stage:#ffffff;
  --frame:#e2e2e2;
}
*{box-sizing:border-box;margin:0;padding:0}
html,body{width:1200px;height:681px;overflow:hidden;background:var(--stage)}
body{font-family:"Montserrat",Arial,sans-serif;color:var(--ink);position:relative}
.stage-frame{position:absolute;left:18px;top:18px;width:1164px;height:636px;border:1px solid var(--frame)}
.sheet{position:absolute;background:var(--paper);box-shadow:2px 3px 8px rgba(0,0,0,.28);overflow:hidden}
.swoosh{position:absolute;display:block}
.brand{display:flex;flex-direction:column;align-items:center;position:absolute}
.brand-row{display:flex;align-items:center;gap:5px}
.brand-dot{border-radius:50%;background:var(--green)}
.brand-name{font-weight:700;color:var(--brand);letter-spacing:.5px;line-height:1}
.brand-tag{font-weight:400;color:var(--brand);letter-spacing:.3px;text-transform:uppercase;white-space:nowrap}

/* envelope front */
.envelope-front{left:67px;top:103px;width:406px;height:209px}
.envelope-front .swoosh{left:0;top:0;width:40px;height:209px}
.envelope-front .brand{left:46px;top:26px}
.envelope-front .brand-dot{width:12px;height:12px}
.envelope-front .brand-name{font-size:22px}
.envelope-front .brand-tag{font-size:4.5px;margin-top:3px}
.return-address{position:absolute;left:38px;bottom:22px;font-size:6px;color:var(--ink);white-space:nowrap}

/* envelope back */
.envelope-back{left:67px;top:343px;width:406px;height:209px}
.envelope-back .flap{position:absolute;left:0;top:0;width:406px;height:80px}
.envelope-back .brand{left:50%;top:84px;transform:translateX(-50%)}
.envelope-back .brand-dot{width:10px;height:10px}
.envelope-back .brand-name{font-size:18px}

/* letterhead */
.letterhead{left:619px;top:43px;width:307px;height:586px}
.letterhead .swoosh{left:0;top:0;width:307px;height:64px}
.letterhead .brand{left:209px;top:68px;transform:translateX(-50%)}
.letterhead .brand-dot{width:12px;height:12px}
.letterhead .brand-name{font-size:22px}
.letterhead .brand-tag{font-size:4.5px;margin-top:3px}
.letter-footer{position:absolute;left:20px;right:0;top:548px;text-align:center;font-size:5px;line-height:1.7;color:var(--ink);white-space:nowrap}

/* business cards */
.card-front{left:970px;top:187px;width:177px;height:106px}
.card-front .swoosh{left:0;top:0;width:24px;height:106px}
.card-holder{position:absolute;right:10px;top:12px;text-align:left;width:74px}
.holder-name{font-size:6px;font-weight:600;color:var(--ink)}
.holder-title{font-size:5px;color:var(--ink);margin-bottom:4px}
.holder-contact{font-size:4px;line-height:1.5;color:var(--ink);white-space:nowrap}
.card-front .brand{left:24px;top:66px}
.card-front .brand-dot{width:7px;height:7px}
.card-front .brand-name{font-size:13px}
.card-front .brand-tag{font-size:3px;margin-top:2px}

.card-back{left:970px;top:314px;width:177px;height:106px}
.service-list{position:absolute;left:38px;top:26px;list-style:none;font-size:5px;line-height:1.75;color:var(--ink);white-space:nowrap}
.service-list li::before{content:"\2022";color:var(--green);margin-right:4px}
</style>
</head>
<body>
<div class="stage-frame"></div>

<section class="sheet envelope-front" aria-label="Envelope front">
  <svg class="swoosh" viewBox="0 0 40 209" preserveAspectRatio="none" aria-hidden="true">
    <path d="M14,0 C2,60 2,150 16,209 L9,209 C-3,150 -3,60 8,0 Z" fill="var(--blue)"/>
    <path d="M24,0 C12,70 13,150 28,209 L24,209 C9,150 8,70 20,0 Z" fill="var(--green)"/>
  </svg>
  <div class="brand">
    <div class="brand-row"><span class="brand-dot"></span><span class="brand-name">Brevard</span></div>
    <span class="brand-tag">Education Technology Consulting</span>
  </div>
  <p class="return-address">517 Alder Lane | Larkmoor, VT 05999</p>
</section>

<section class="sheet envelope-back" aria-label="Envelope back">
  <svg class="flap" viewBox="0 0 406 80" preserveAspectRatio="none" aria-hidden="true">
    <path d="M0,1 L190,64 Q203,69 216,64 L406,1" fill="none" stroke="#9a9a9a" stroke-width="1"/>
  </svg>
  <div class="brand">
    <div class="brand-row"><span class="brand-dot"></span><span class="brand-name">Brevard</span></div>
  </div>
</section>

<section class="sheet letterhead" aria-label="Letterhead">
  <svg class="swoosh" viewBox="0 0 307 64" preserveAspectRatio="none" aria-hidden="true">
    <path d="M0,44 C70,14 170,2 250,4 C170,10 80,26 0,56 Z" fill="var(--blue)"/>
    <path d="M40,44 C120,18 220,12 307,14 L307,21 C220,19 130,26 40,46 Z" fill="var(--green)"/>
  </svg>
  <div class="brand">
    <div class="brand-row"><span class="brand-dot"></span><span class="brand-name">Brevard</span></div>
    <span class="brand-tag">Education Technology Consulting</span>
  </div>
  <div class="letter-footer">
    <p>517 Alder Lane | Larkmoor, VT 05999</p>
    <p>Phone: 555-014-0172 | Email: owen@pelmarconsult.example | www.pelmarconsult.example</p>
  </div>
</section>

<section class="sheet card-front" aria-label="Business card front">
  <svg class="swoosh" viewBox="0 0 24 106" preserveAspectRatio="none" aria-hidden="true">
    <path d="M9,0 C1,30 1,76 10,106 L5,106 C-2,76 -2,30 4,0 Z" fill="var(--blue)"/>
    <path d="M15,0 C7,34 8,76 17,106 L14,106 C4,76 4,34 12,0 Z" fill="var(--green)"/>
  </svg>
  <div class="card-holder">
    <p class="holder-name">Owen P. Marsh</p>
    <p class="holder-title">Consultant</p>
    <p class="holder-contact">517 Alder Lane<br>Larkmoor, VT 05999<br>555-014-0172<br>owen@pelmarconsult.example<br>www.pelmarconsult.example</p>
  </div>
  <div class="brand">
    <div class="brand-row"><span class="brand-dot"></span><span class="brand-name">Brevard</span></div>
    <span class="brand-tag">Education Technology Consulting</span>
  </div>
</section>

<section class="sheet card-back" aria-label="Business card back">
  <ul class="service-list">
    <li>Technology Plan Creation</li>
    <li>Education Technology Support</li>
    <li>Teacher Professional Development</li>
    <li>Budgeting</li>
    <li>IT Support</li>
  </ul>
</section>
</body>
</html>
```